Business Card & Stationary for Jeweller | ||
Pearl Marquise Inc. | ||
Use same font as used in my logo | ||
Modern Professional Bright & Fun-filled |
Lorraine Whitcombe | ||
President & Principal Designer | ||
By Appointment | ||
lwhitcombe@pearlmarquise-example.ca | ||
www.pearlmarquise-example.ca | ||
Please add: Chatterbook Logo plus www.chatterbook-example.com/PearlMarquiseGems Chirpline Logo plus @RovingGemsmith NCF (National Crystalline Foundation) Logo Ethical Gemcraft Alliance Logo **I would like to incorporate a white background with black polka dots somehow on both the business card and stationary. I want glamour, trendy, feminine.** |
We customize each design experience to the clients requirements and bring our expertise and design tools to you! Complimentary Diamond Insurance for 12 months after purchase. Lifetime Manufacturing Warranty Free Lifetime Trade-Up Program Complimentary Champagne Delivery by Appointment Included |

```html
<!DOCTYPE html>
<html lang="en">
<head>
<meta charset="utf-8">
<title>Pearl Marquise Inc. – Business Card</title>
<link rel="stylesheet" href="https://fonts.googleapis.com/css2?family=Cormorant+SC:wght@500&family=Open+Sans:wght@400&display=swap">
<style>
  :root {
    --backdrop: #ecebe8;
    --card-white: #ffffff;
    --slate-dark: #27333c;
    --slate-mid: #44535e;
    --slate-light: #5b6a75;
    --rule-grey: #d6d9dc;
    --text-grey: #7b7f84;
    --accent-pink: #e7679a;
    --back-pink: #f47ea7;
    --band-grey: #9a9a9c;
  }
  * { box-sizing: border-box; margin: 0; padding: 0; }
  html, body {
    width: 1200px; height: 896px; overflow: hidden;
    background: var(--backdrop);
    font-family: "Open Sans", Arial, sans-serif;
  }
  .stage { position: relative; width: 1200px; height: 896px; }

  .card {
    position: absolute; width: 560px; height: 320px;
    box-shadow: 0 6px 18px rgba(0,0,0,.22);
    overflow: hidden;
  }

  /* Front */
  .card-front { left: 70px; top: 80px; background: var(--card-white); }
  .front-band {
    position: absolute; left: 0; top: 0; width: 100%; height: 175px;
    background: radial-gradient(ellipse at 50% 45%, var(--slate-light) 0%, var(--slate-mid) 45%, var(--slate-dark) 100%);
  }
  .brand {
    position: absolute; left: 0; top: 0; width: 100%; height: 175px;
    display: flex; align-items: center; justify-content: center; gap: 12px;
  }
  .brand-dot { width: 12px; height: 12px; border-radius: 50%; background: #ffffff; }
  .brand-name {
    font-family: "Cormorant SC", Georgia, serif; font-weight: 500;
    font-size: 30px; color: #ffffff; letter-spacing: 1px;
  }
  .front-fade {
    position: absolute; left: 0; top: 175px; width: 100%; height: 14px;
    background: linear-gradient(180deg, var(--rule-grey), var(--card-white));
  }
  .person { position: absolute; left: 40px; top: 212px; }
  .person-name {
    font-family: "Cormorant SC", Georgia, serif; font-weight: 500;
    font-size: 21px; color: var(--accent-pink); letter-spacing: .5px;
  }
  .person-title { font-size: 11px; color: var(--text-grey); margin-top: 2px; }

  .contacts { position: absolute; left: 290px; top: 214px; list-style: none; }
  .contacts li {
    display: flex; align-items: center; gap: 9px; white-space: nowrap;
    font-size: 11px; color: var(--text-grey); height: 21px;
  }
  .contacts svg { width: 13px; height: 13px; flex: none; }

  /* Back */
  .card-back { left: 570px; top: 500px; background: var(--back-pink); }
  .back-copy { position: absolute; left: 26px; top: 26px; right: 30px; color: #ffffff; font-size: 13px; line-height: 1.45; }
  .back-copy p { margin-bottom: 13px; }
  .back-band {
    position: absolute; right: 0; bottom: 14px; width: 250px; height: 16px;
    background: var(--band-grey);
    clip-path: polygon(18px 0, 100% 0, 100% 100%, 0 100%);
  }
</style>
</head>
<body>
<main class="stage">
  <section class="card card-front" aria-label="Business card front">
    <div class="front-band" role="img" aria-label="Dark slate textured header backdrop"></div>
    <div class="brand">
      <span class="brand-dot"></span>
      <span class="brand-name">Pearl Marquise</span>
    </div>
    <div class="front-fade"></div>
    <div class="person">
      <div class="person-name">Lorraine Whitcombe</div>
      <div class="person-title">President &amp; Principal Designer</div>
    </div>
    <ul class="contacts">
      <li>
        <svg viewBox="0 0 14 14"><circle cx="7" cy="7" r="7" fill="#e7679a"/><path d="M4.5 3.5l1.6 1.6-.9 1.1a5 5 0 0 0 2.6 2.6l1.1-.9 1.6 1.6-1 1c-2.8 0-6-3.2-6-6z" fill="#fff"/></svg>
        1-555-010-4422
      </li>
      <li>
        <svg viewBox="0 0 14 14"><circle cx="7" cy="7" r="7" fill="#e7679a"/><path d="M4.5 3.5l1.6 1.6-.9 1.1a5 5 0 0 0 2.6 2.6l1.1-.9 1.6 1.6-1 1c-2.8 0-6-3.2-6-6z" fill="#fff"/></svg>
        1-555-010-4423
      </li>
      <li>
        <svg viewBox="0 0 14 14"><circle cx="7" cy="7" r="7" fill="#e7679a"/><rect x="3.5" y="4.5" width="7" height="5" fill="none" stroke="#fff" stroke-width="1"/><path d="M3.5 4.5L7 7.3l3.5-2.8" fill="none" stroke="#fff" stroke-width="1"/></svg>
        lwhitcombe@pearlmarquise-example.ca
      </li>
    </ul>
  </section>

  <section class="card card-back" aria-label="Business card back">
    <div class="back-copy">
      <p>We customize each design experience to the clients requirements and bring our expertise and design tools to you!</p>
      <p>Complimentary Diamond Insurance for 12 months after purchase.</p>
      <p>Lifetime Manufacturing Warranty</p>
      <p>Free Lifetime Trade-Up Program</p>
      <p>Complimentary Champagne</p>
      <p>Delivery by Appointment Included</p>
    </div>
    <div class="back-band"></div>
  </section>
</main>
</body>
</html>
```